Environmentally conscious Waste Management Company requires business card

We Require a Business card for our environmentally conscious waste management company . The business card should have a very clean design. be double sided and incorporate our logo..
The card will need o have 9 lines for the contact details - that are
Name
Title
Business
Address Line 1
Address Line 2
Address Line 3
Phone
Mobile
Email

Industry/Entity Type

Waste Management

Other font styles liked:
• Helvetica or similar

```html
<!DOCTYPE html>
<html lang="en">
<head>
<meta charset="UTF-8">
<title>Clearbins Business Card</title>
<link rel="stylesheet" href="https://fonts.googleapis.com/css2?family=Inter:ital,wght@0,400;0,600;1,600&family=Michroma&display=swap">
<style>
  :root {
    --backdrop: #e6e6e4;
    --card: #f4f4f3;
    --green: #22b53c;
    --ink: #2b2b2b;
    --ink-soft: #555555;
    --shadow: rgba(0, 0, 0, 0.14);
  }
  * { box-sizing: border-box; margin: 0; padding: 0; }
  html, body {
    width: 1200px;
    height: 900px;
    overflow: hidden;
    background: var(--backdrop);
  }
  .canvas {
    position: relative;
    width: 1200px;
    height: 900px;
    display: flex;
    flex-direction: column;
    align-items: center;
    justify-content: center;
    gap: 56px;
  }
  .card {
    position: relative;
    width: 640px;
    height: 366px;
    background: var(--card);
    box-shadow: 0 6px 18px var(--shadow);
    font-family: "Inter", Helvetica, Arial, sans-serif;
    color: var(--ink);
  }
  .brand {
    display: flex;
    align-items: center;
    gap: 10px;
  }
  .brand-dot {
    width: 14px;
    height: 14px;
    border-radius: 50%;
    background: var(--green);
  }
  .brand-name {
    font-family: "Inter", Helvetica, Arial, sans-serif;
    font-weight: 600;
    font-size: 30px;
    letter-spacing: 0.5px;
    color: var(--ink);
    line-height: 1;
  }
  .card-front .brand {
    position: absolute;
    left: 50%;
    top: 50%;
    transform: translate(-50%, -50%);
  }
  .card-back .brand {
    position: absolute;
    left: 40px;
    top: 44px;
  }
  .company-block {
    position: absolute;
    left: 40px;
    top: 112px;
    font-size: 11px;
    font-style: normal;
    line-height: 1.75;
    letter-spacing: 0.8px;
    color: var(--ink-soft);
  }
  .company-name {
    font-weight: 600;
    font-style: italic;
    color: var(--ink);
  }
  .person {
    position: absolute;
    right: 44px;
    top: 200px;
    text-align: right;
    font-family: "Michroma", "Inter", sans-serif;
  }
  .person-name {
    font-size: 20px;
    letter-spacing: 4px;
    color: var(--ink);
  }
  .person-title {
    margin-top: 4px;
    font-size: 12px;
    letter-spacing: 3px;
    color: var(--green);
  }
  .contact-list {
    position: absolute;
    right: 44px;
    bottom: 36px;
    list-style: none;
    font-size: 11px;
    letter-spacing: 1.2px;
    color: var(--ink-soft);
  }
  .contact-item {
    display: flex;
    justify-content: flex-end;
    align-items: center;
    gap: 12px;
    height: 20px;
  }
  .contact-icon {
    width: 13px;
    height: 13px;
    flex: none;
  }
  .contact-icon * {
    fill: none;
    stroke: var(--green);
    stroke-width: 1.6;
    stroke-linejoin: round;
    stroke-linecap: round;
  }
</style>
</head>
<body>
<main class="canvas">
  <section class="card card-front" aria-label="Card front">
    <div class="brand">
      <span class="brand-dot"></span>
      <span class="brand-name">Clearbins</span>
    </div>
  </section>

  <section class="card card-back" aria-label="Card back">
    <div class="brand">
      <span class="brand-dot"></span>
      <span class="brand-name">Clearbins</span>
    </div>

    <address class="company-block">
      <div class="company-name">Clearbin Works, Pty Ltd</div>
      <div>Address Line 1</div>
      <div>Address Line 2</div>
      <div>Address Line 3</div>
    </address>

    <div class="person">
      <div class="person-name">Mara Lind</div>
      <div class="person-title">Title</div>
    </div>

    <ul class="contact-list">
      <li class="contact-item">
        <span>999 999 9999</span>
        <svg class="contact-icon" viewBox="0 0 14 14" aria-label="Phone">
          <path d="M2 5 Q7 1 12 5 L10.5 6.5 L9 5.5 L5 5.5 L3.5 6.5 Z"/>
          <rect x="3.5" y="7.5" width="7" height="4.5" rx="0.8"/>
        </svg>
      </li>
      <li class="contact-item">
        <span>999 999 9999</span>
        <svg class="contact-icon" viewBox="0 0 14 14" aria-label="Mobile">
          <rect x="3.5" y="1.5" width="7" height="11" rx="1"/>
          <path d="M6 10.5 H8"/>
        </svg>
      </li>
      <li class="contact-item">
        <span>mara@clearbins.com</span>
        <svg class="contact-icon" viewBox="0 0 14 14" aria-label="Email">
          <rect x="1.5" y="3" width="11" height="8" rx="0.6"/>
          <path d="M1.5 3.5 L7 8 L12.5 3.5"/>
        </svg>
      </li>
    </ul>
  </section>
</main>
</body>
</html>
```